Design a DL Size invitation for End of Year Celebration

Looking for a design to be created for end of year invitation to go to staff and key stakeholders. Invite is to an afternoon sailing Sydney Harbour on a catamaran. The design should demonstrate quality, a bit of fun and is to be printed on white ("velbrook oxwen" paper stock - you can google this if you need to see it).

I will attach below a copy of our logo in AI / pdf format (please note that attached logo has a cream background - this should be removed before placing in any new artwork)

Dimensions for the artwork should be DL size (210 x 99) with a 3mm bleed in CYMK

Front side - invitation with a place for full name to be added. If artwork is supplied in AI or editable PDF we will update with the individual names.
Reverse side - mainly for details of the event and where to RSVP. This size will not need to be customised for each invitee

```html
<!DOCTYPE html>
<html lang="en">
<head>
<meta charset="utf-8">
<title>Celebrate &amp; Collaborate 2013 – Invitation</title>
<link href="https://fonts.googleapis.com/css2?family=Montserrat:wght@300;400&family=Schoolbell&display=swap" rel="stylesheet">
<style>
  :root {
    --canvas: #ececec;
    --paper: #ffffff;
    --harbour-cyan: #00b9ef;
    --sun-yellow: #f3e21a;
    --ink-blue: #1b9ad8;
    --photo-light: #f4f4f4;
    --photo-mid: #dcdcdc;
    --photo-dark: #c9c9c9;
  }
  * { margin: 0; padding: 0; box-sizing: border-box; }
  html, body {
    width: 1200px;
    height: 709px;
    overflow: hidden;
    background: var(--canvas);
    font-family: "Montserrat", sans-serif;
  }
  .invitation-card {
    position: absolute;
    left: 240px;
    width: 720px;
    height: 340px;
    background: var(--paper);
    overflow: hidden;
    box-shadow: 0 1px 3px rgba(0,0,0,0.12);
  }
  .card-front { top: 10px; }
  .card-reverse { top: 359px; }

  .harbour-photo {
    position: absolute;
    inset: 0;
    background:
      radial-gradient(ellipse 60% 70% at 62% 45%, var(--photo-mid) 0%, rgba(220,220,220,0.5) 45%, rgba(255,255,255,0) 75%),
      linear-gradient(180deg, var(--paper) 0%, var(--photo-light) 55%, var(--paper) 100%);
    opacity: 0.9;
  }

  /* Front */
  .title-band {
    position: absolute;
    left: 0;
    top: 25px;
    width: 469px;
    height: 126px;
    background: var(--harbour-cyan);
  }
  .event-title {
    position: absolute;
    left: 22px;
    top: 14px;
    color: var(--sun-yellow);
    font-weight: 300;
    font-size: 47px;
    line-height: 46px;
    letter-spacing: -0.5px;
  }
  .event-year {
    position: absolute;
    left: 418px;
    top: 18px;
    color: var(--paper);
    font-weight: 300;
    font-size: 36px;
    line-height: 1;
    writing-mode: vertical-rl;
    letter-spacing: 1px;
  }
  .event-summary {
    position: absolute;
    left: 22px;
    top: 172px;
    width: 640px;
    color: var(--ink-blue);
    font-size: 22.5px;
    line-height: 27px;
  }
  .guest-name {
    position: absolute;
    left: 22px;
    top: 292px;
    color: var(--ink-blue);
    font-family: "Schoolbell", cursive;
    font-size: 19px;
    letter-spacing: 1.5px;
  }

  /* Reverse */
  .detail-group {
    position: absolute;
    color: var(--ink-blue);
    font-size: 13px;
    line-height: 19px;
  }
  .detail-heading {
    color: var(--sun-yellow);
    font-weight: 400;
    font-size: 22px;
    line-height: 26px;
    margin-bottom: 3px;
  }
  .detail-date { left: 25px; top: 42px; }
  .detail-time { left: 25px; top: 120px; }
  .detail-dress { left: 348px; top: 42px; }
  sup { font-size: 8px; line-height: 0; }
</style>
</head>
<body>

<section class="invitation-card card-front">
  <div class="harbour-photo" role="img" aria-label="Faded black and white photograph of Sydney Harbour Bridge with ferries on the water"></div>
  <div class="title-band">
    <h1 class="event-title">Celebrate &amp;<br>Collaborate</h1>
    <span class="event-year">2013</span>
  </div>
  <p class="event-summary">An afternoon aboard the 48’ sailing catamaran Seabright touring the spectacular Sydney Harbour including with a gourmet BBQ and drinks.</p>
  <p class="guest-name">Name Mara Keel</p>
</section>

<section class="invitation-card card-reverse">
  <div class="harbour-photo" role="img" aria-label="Faded black and white photograph of Sydney Harbour Bridge"></div>
  <div class="detail-group detail-date">
    <h2 class="detail-heading">Date</h2>
    <p>Thursday<br>19<sup>th</sup> December 2013</p>
  </div>
  <div class="detail-group detail-time">
    <h2 class="detail-heading">Time</h2>
    <p>12.00pm Meet at wharf<br>(located on the eastern pier)<br>12.30pm Depart wharf<br>4.30pm Return to wharf</p>
  </div>
  <div class="detail-group detail-dress">
    <h2 class="detail-heading">Dress</h2>
    <p>Casual summer boatattire<br>(stiletto heels cannot be worn)</p>
  </div>
</section>

</body>
</html>
```